Typing Service Business Card Design

Need a new business card design for new logo update. The Keyline Crew is an outsourced typing service. We type audio / voice files into word documents. We are a professional service that is recognised in the industry over the past 15 years and have a strong connection to our brand. The final design should be professional, simple, yet effective.

Business

Contact Information for Business Card

Rosalind Varga
Director

rosalind@kbq.com.au
www.thekeylinecrewbase.com.au

```html
<!DOCTYPE html>
<html lang="en">
<head>
<meta charset="utf-8">
<title>The Keyline Crew – Business Card</title>
<link rel="stylesheet" href="https://fonts.googleapis.com/css2?family=Montserrat:wght@400;500;700&display=swap">
<style>
  :root {
    --backdrop: #e4e4e6;
    --card: #1f1f22;
    --pink: #d9479f;
    --white: #f4f4f4;
    --text-font: "Montserrat", sans-serif;
  }
  * { margin: 0; padding: 0; box-sizing: border-box; }
  html, body {
    width: 1200px;
    height: 1189px;
    overflow: hidden;
    background: var(--backdrop);
  }
  .card {
    position: absolute;
    left: 150px;
    width: 900px;
    height: 514px;
    background: var(--card);
    border-radius: 34px;
    color: var(--white);
    font-family: var(--text-font);
  }
  .card--back { top: 54px; }
  .card--front { top: 621px; }

  .brand-name {
    position: absolute;
    font-family: var(--text-font);
    font-weight: 700;
    color: var(--pink);
    white-space: nowrap;
    letter-spacing: -0.5px;
  }
  .slogan {
    position: absolute;
    font-family: var(--text-font);
    font-weight: 400;
    color: var(--white);
    white-space: nowrap;
  }

  /* back side */
  .card--back .brand-name { left: 0; right: 0; top: 150px; text-align: center; font-size: 62px; }
  .card--back .slogan { left: 0; right: 0; top: 240px; text-align: center; font-size: 30px; }
  .card--back .web-address {
    position: absolute; left: 0; right: 0; top: 360px;
    text-align: center; font-size: 20px; letter-spacing: 1px;
  }

  /* front side */
  .card--front .brand-name { left: 60px; top: 78px; font-size: 54px; }
  .card--front .slogan { left: 230px; top: 160px; font-size: 28px; }
  .person { position: absolute; right: 70px; top: 210px; text-align: right; }
  .person__name { font-size: 30px; font-weight: 500; letter-spacing: 1px; }
  .person__role { font-size: 22px; color: var(--pink); margin-top: 6px; letter-spacing: 1px; }
  .divider {
    position: absolute; left: 60px; right: 200px; top: 262px;
    height: 2px; background: var(--pink);
  }
  .abn { position: absolute; right: 70px; top: 312px; font-size: 26px; letter-spacing: 1px; }
  .abn__label { color: var(--pink); margin-right: 22px; }
  .contact-list { position: absolute; left: 60px; top: 360px; list-style: none; }
  .contact-list li {
    display: flex; align-items: center; gap: 14px;
    font-size: 26px; letter-spacing: 0.5px; height: 44px;
  }
  .contact-icon { width: 32px; height: 32px; flex: none; }
</style>
</head>
<body>

<section class="card card--back" aria-label="Card back">
  <div class="brand-name">The Keyline Crew</div>
  <div class="slogan">Voice in. Text out.</div>
  <div class="web-address">www.thekeylinecrewbase.com.au</div>
</section>

<section class="card card--front" aria-label="Card front">
  <div class="brand-name">The Keyline Crew</div>
  <div class="slogan">Voice in. Text out.</div>

  <div class="person">
    <div class="person__name">Rosalind Varga</div>
    <div class="person__role">Director</div>
  </div>
  <div class="divider"></div>

  <div class="abn"><span class="abn__label">ABN:</span>47 902 318 665</div>

  <ul class="contact-list">
    <li>
      <svg class="contact-icon" viewBox="0 0 32 32" aria-hidden="true">
        <rect width="32" height="32" rx="4" fill="#d9479f"/>
        <path d="M11 8c-2 1-3 3-2 6 2 5 5 8 9 10 3 1 5 0 6-2l-3-3-2 2c-2-1-4-3-5-5l2-2-3-4z" fill="#1f1f22"/>
      </svg>
      <span>555 018 2047</span>
    </li>
    <li>
      <svg class="contact-icon" viewBox="0 0 32 32" aria-hidden="true">
        <rect width="32" height="32" rx="4" fill="#d9479f"/>
        <rect x="6" y="9" width="20" height="14" fill="none" stroke="#1f1f22" stroke-width="2"/>
        <path d="M6 9l10 8 10-8" fill="none" stroke="#1f1f22" stroke-width="2"/>
      </svg>
      <span>rosalind@kbq.com.au</span>
    </li>
    <li>
      <svg class="contact-icon" viewBox="0 0 32 32" aria-hidden="true">
        <rect width="32" height="32" rx="4" fill="#d9479f"/>
        <g fill="none" stroke="#1f1f22" stroke-width="1.8">
          <circle cx="16" cy="16" r="9"/>
          <ellipse cx="16" cy="16" rx="4" ry="9"/>
          <path d="M7 16h18M9 11h14M9 21h14"/>
        </g>
      </svg>
      <span>www.thekeylinecrewbase.com.au</span>
    </li>
  </ul>
</section>

</body>
</html>
```